Quorvel Lab - Business Cards & Stationary
Layouts for B-cards, Letterhead, Powerpoint Templates
Quorvel Lab - Business Cards & Stationary -
Creative Brief
Professional
Desmond Pelly
Director of Product Development
4852 Amberfield Lane Dallas, Texas 75391-4418
des.pelly@quorvellabs.example

```html
<!DOCTYPE html>
<html lang="en">
<head>
<meta charset="utf-8">
<title>Quorvel Lab – Business Cards</title>
<link rel="stylesheet" href="https://fonts.googleapis.com/css2?family=Arimo:wght@400;700&display=swap">
<style>
  :root {
    --stage: #e9e6e2;
    --card-light: #ffffff;
    --card-light-shade: #e4e4e4;
    --card-dark: #0c0b0b;
    --card-dark-shade: #2a2522;
    --gold: #8a6a2a;
    --gold-light: #b8944a;
    --ink: #1c1c1c;
    --ink-soft: #555555;
    --paper-text: #d9d9d9;
    --accent-red: #a3121c;
    --accent-red-dark: #5e0a10;
  }
  * { box-sizing: border-box; margin: 0; padding: 0; }
  html, body { width: 1200px; height: 911px; overflow: hidden; }
  body {
    background: var(--stage);
    font-family: "Arimo", Arial, sans-serif;
    position: relative;
  }
  .card {
    position: absolute;
    width: 520px;
    height: 300px;
    border-radius: 14px;
    overflow: hidden;
    box-shadow: 0 6px 18px rgba(0,0,0,.18);
  }
  .card--light { background: linear-gradient(135deg, var(--card-light) 55%, var(--card-light-shade)); }
  .card--dark  { background: linear-gradient(135deg, var(--card-dark) 55%, var(--card-dark-shade)); }
  .front-light { left: 60px;  top: 100px; }
  .front-dark  { left: 620px; top: 100px; }
  .back-light  { left: 60px;  top: 510px; }
  .back-dark   { left: 620px; top: 510px; }

  .decor {
    position: absolute;
    right: 20px;
    top: 60px;
    width: 230px;
    height: 230px;
    border-radius: 50%;
  }
  .card--light .decor { background: radial-gradient(circle, rgba(0,0,0,.07), rgba(0,0,0,.02)); }
  .card--dark .decor  { background: radial-gradient(circle, rgba(255,255,255,.08), rgba(255,255,255,.02)); }

  .wordmark {
    position: absolute;
    left: 40px;
    top: 42px;
    display: flex;
    align-items: center;
    gap: 14px;
  }
  .wordmark__dot {
    width: 46px; height: 46px; border-radius: 50%;
    background: var(--gold);
  }
  .wordmark__name {
    font-size: 44px;
    font-weight: 400;
    color: var(--gold);
    letter-spacing: -.5px;
  }
  .contact {
    position: absolute;
    left: 110px;
    top: 150px;
    display: flex;
    align-items: flex-start;
    font-size: 11px;
    line-height: 1.45;
  }
  .contact__person { text-align: right; padding-right: 14px; padding-top: 8px; width: 180px; }
  .contact__name { font-size: 15px; font-weight: 700; }
  .contact__title { font-size: 10px; }
  .contact__rule { width: 1px; height: 76px; }
  .contact__details { padding-left: 14px; }
  .card--light .contact { color: var(--ink-soft); }
  .card--light .contact__name { color: var(--ink); }
  .card--light .contact__rule { background: #999; }
  .card--dark .contact { color: var(--paper-text); }
  .card--dark .contact__name { color: #fff; }
  .card--dark .contact__rule { background: #777; }

  .swoosh { position: absolute; left: 0; bottom: 0; width: 520px; height: 40px; }

  .back-mark {
    position: absolute;
    right: 30px; bottom: 28px;
    width: 40px; height: 40px; border-radius: 50%;
    background: var(--gold-light);
  }
</style>
</head>
<body>

  <section class="card card--light front-light" aria-label="Business card front, light">
    <div class="decor" role="img" aria-label="Faint brand decoration"></div>
    <div class="wordmark"><span class="wordmark__dot"></span><span class="wordmark__name">Quorvel Labs</span></div>
    <div class="contact">
      <div class="contact__person">
        <p class="contact__name">Desmond Pelly</p>
        <p class="contact__title">Director of Product Development</p>
      </div>
      <div class="contact__rule"></div>
      <div class="contact__details">
        <p>4852 Amberfield Lane</p>
        <p>Dallas, Texas 75391-4418</p>
        <p>Cell: &nbsp;817 555 0142</p>
        <p>Email: des.pelly@quorvellabs.example</p>
      </div>
    </div>
    <svg class="swoosh" viewBox="0 0 520 40" preserveAspectRatio="none" aria-hidden="true">
      <path d="M0 40 L0 34 C180 34 330 30 520 6 L520 40 Z" fill="var(--accent-red)"/>
      <path d="M0 40 L0 37 C200 37 350 34 520 16 L520 40 Z" fill="var(--accent-red-dark)"/>
    </svg>
  </section>

  <section class="card card--dark front-dark" aria-label="Business card front, dark">
    <div class="decor" role="img" aria-label="Faint brand decoration"></div>
    <div class="wordmark"><span class="wordmark__dot"></span><span class="wordmark__name">Quorvel Labs</span></div>
    <div class="contact">
      <div class="contact__person">
        <p class="contact__name">Desmond Pelly</p>
        <p class="contact__title">Director of Product Development</p>
      </div>
      <div class="contact__rule"></div>
      <div class="contact__details">
        <p>4852 Amberfield Lane</p>
        <p>Dallas, Texas 75391-4418</p>
        <p>Cell: &nbsp;817 555 0142</p>
        <p>Email: des.pelly@quorvellabs.example</p>
      </div>
    </div>
    <svg class="swoosh" viewBox="0 0 520 40" preserveAspectRatio="none" aria-hidden="true">
      <path d="M0 40 L0 34 C180 34 330 30 520 6 L520 40 Z" fill="var(--accent-red)"/>
      <path d="M0 40 L0 37 C200 37 350 34 520 16 L520 40 Z" fill="var(--accent-red-dark)"/>
    </svg>
  </section>

  <section class="card card--light back-light" aria-label="Business card back, light">
    <div class="decor" role="img" aria-label="Faint brand decoration"></div>
    <span class="back-mark"></span>
  </section>

  <section class="card card--dark back-dark" aria-label="Business card back, dark">
    <div class="decor" role="img" aria-label="Faint brand decoration"></div>
    <span class="back-mark"></span>
  </section>

</body>
</html>
```